Journeys With Marlowe Business Cards

I need a business card design for my upscale Travel Agency.
Attached you can find my logo.
I would like to include the following:
- Name
- Title
- Phone Number
- Email
- Website
- and then something like: Follow us: JourneysWithMarlowe (and then social media icons in color).
The logo should be in the front and then also the back.
I am also attaching a design that I liked (mostly for the layout) but open to any suggestions
Industry/Entity Type
Travel Agent
Contact Information for Business Card
Name: Celine Drummond
Title: Travel Designer / Owner
Phone: 415-296-0487
Email: celine@journeyswithmarlowe.example
Website: www.JourneysWithMarlowe.example
Social Media Handles for FB,IG, Twitter: JourneysWithMarlowe
Font styles to use
Colors
Designer to choose colors to be used in the design.
Look and feel

```html
<!DOCTYPE html>
<html lang="en">
<head>
<meta charset="utf-8">
<title>Journeys With Marlowe – Business Cards</title>
<link rel="stylesheet" href="https://fonts.googleapis.com/css2?family=Montserrat:wght@400;500;700&display=swap">
<style>
  :root {
    --stage: #1d1d1d;
    --card-dark: #1b1b1b;
    --card-light: #ffffff;
    --accent: #f5a552;
    --ink: #2b2b2b;
    --muted: #9a9a9a;
  }
  * { box-sizing: border-box; margin: 0; padding: 0; }
  html, body { width: 1200px; height: 852px; overflow: hidden; }
  body {
    background: var(--stage);
    font-family: "Montserrat", sans-serif;
    position: relative;
  }
  .card {
    position: absolute;
    left: 300px;
    width: 600px;
    height: 343px;
    border-radius: 18px;
    overflow: hidden;
  }
  .card--back { top: 50px; background: var(--card-dark); }
  .card--front { top: 450px; background: var(--card-light); color: var(--ink); }

  .brand { display: flex; align-items: center; gap: 14px; position: absolute; }
  .brand__mark { background: var(--accent); }
  .brand__name { color: var(--accent); font-weight: 500; white-space: nowrap; }

  .card--back .brand { left: 50%; top: 50%; transform: translate(-50%, -50%); }
  .card--back .brand__mark { width: 42px; height: 42px; }
  .card--back .brand__name { font-size: 30px; }

  .card--front .brand { left: 36px; top: 34px; }
  .card--front .brand__mark { width: 24px; height: 24px; }
  .card--front .brand__name { font-size: 18px; }

  .shapes { position: absolute; inset: 0; }

  .social { position: absolute; right: 40px; top: 40px; text-align: right; }
  .social__chip { display: inline-block; width: 24px; height: 24px; border-radius: 5px; background: var(--accent); margin-bottom: 6px; }
  .social__text { font-size: 13px; padding-bottom: 6px; border-bottom: 1.5px solid var(--accent); }

  .address { position: absolute; right: 40px; top: 110px; text-align: right; font-size: 13px; line-height: 1.5; }

  .person { position: absolute; left: 40px; top: 150px; }
  .person__name { color: var(--accent); font-weight: 700; font-size: 24px; letter-spacing: 0.5px; text-transform: uppercase; }
  .person__title { font-size: 14px; margin-top: 2px; padding-bottom: 12px; border-bottom: 1.5px solid var(--accent); width: 240px; }

  .contacts { position: absolute; left: 40px; top: 232px; list-style: none; font-size: 13.5px; }
  .contacts li { display: flex; align-items: center; gap: 10px; line-height: 23px; }
  .contacts svg { width: 13px; height: 13px; fill: none; stroke: var(--accent); stroke-width: 2; }
  .contacts .hl { color: var(--accent); }
</style>
</head>
<body>

  <section class="card card--back">
    <div class="brand">
      <span class="brand__mark"></span>
      <span class="brand__name">Journeys With Marlowe</span>
    </div>
  </section>

  <section class="card card--front">
    <svg class="shapes" viewBox="0 0 600 343" aria-hidden="true">
      <polygon points="400,343 420,255 600,255 600,343" fill="var(--accent)"/>
      <polygon points="330,343 400,343 420,255 400,255" fill="#cfcfcf"/>
    </svg>

    <div class="brand">
      <span class="brand__mark"></span>
      <span class="brand__name">Journeys With Marlowe</span>
    </div>

    <div class="social">
      <span class="social__chip"></span>
      <p class="social__text">Follow us: JourneysWithMarlowe</p>
    </div>

    <address class="address" style="font-style:normal">
      218 Juniper Crest<br>Drive Reno, NV 89501
    </address>

    <div class="person">
      <h1 class="person__name">Celine Drummond</h1>
      <p class="person__title">Travel Designer / Owner</p>
    </div>

    <ul class="contacts">
      <li><svg viewBox="0 0 16 16"><path d="M4 2l3 3-2 2c1 2 2 3 4 4l2-2 3 3-2 2C7 14 2 9 2 4z"/></svg>415-296-0487</li>
      <li><svg viewBox="0 0 16 16"><rect x="2" y="4" width="12" height="9"/><path d="M2 4l6 5 6-5"/></svg>celine@journeyswithmarlowe.example</li>
      <li><svg viewBox="0 0 16 16"><circle cx="8" cy="8" r="6"/><path d="M2 8h12M8 2c3 3 3 9 0 12M8 2c-3 3-3 9 0 12"/></svg>www.<span class="hl">JourneysWithMarlowe</span>.example</li>
    </ul>
  </section>

</body>
</html>
```